Flyer for swimming pool service business

I am starting up a new pool cleaning business and I'm focusing on suburbs surrounding my suburb. So it will be a local service with fast, professional and friendly service.. I would like a Flyer of A5 size to drop into letterboxes local homes.

The business is called 'Gumleaf Spa Care'

The following is what I would like in the flyer

Pool service frustrating you?
Troubled by poor water condition?
Tired of doing it yourself?

Keep your swimming pool sparkling and safe all year round

- water testing
- pool chemistry
- chlorine levels
- Ph balance
- equipment maintenance
- algae prevention
- leaf and debris maintenance
- filter cleaning
- tile cleaning
- salt water systems
- local service
- chemicals supplied and delivered
All for the low price of $40 a month (plus chemicals)

Relax and let Gumleaf Spa Care take care of it for you.
for a one off service or a monthly service
no contracts

Contact details
Mitch - 0417 283 640
gumleafspacare@quollmail.net.au

Target Market(s)

the target market is a couples and familys 40-70 years old in a well off riverside suburb

Industry/Entity Type

Pool Service

Requirements
Must have
• Am looking to have a nice blue crystal clear water as part of the background either big or small.

Include my logo (provided) feel free to change the font of the Gumleaf Spas Care writing on it, if that suits your design
Should not have
• cartoonish or funny images

```html
<!DOCTYPE html>
<html lang="en">
<head>
<meta charset="utf-8">
<title>Gumleaf Spa Care – Flyer</title>
<link rel="stylesheet" href="https://fonts.googleapis.com/css2?family=Crimson+Pro:wght@500&family=PT+Sans+Narrow:wght@400;700&display=swap">
<style>
  :root {
    --backdrop: #dcdde0;
    --stone-light: #d9d4cc;
    --stone-dark: #a9a399;
    --leaf-light: #a7b94a;
    --leaf-mid: #5f7a22;
    --leaf-dark: #2c3c12;
    --cream: #f3f1e4;
    --pool-light: #6fd0ec;
    --pool-mid: #3fb3dc;
    --pool-deep: #1e8fc4;
    --headline-blue: #2a7bbf;
    --navy: #1c2a4a;
    --price-blue: #2f4fa8;
    --price-red: #c8362e;
    --white: #ffffff;
  }
  * { margin: 0; padding: 0; box-sizing: border-box; }
  html, body {
    width: 1200px; height: 900px; overflow: hidden;
    background: var(--backdrop);
  }
  .flyer {
    position: absolute; left: 300px; top: 20px;
    width: 600px; height: 860px;
    background: linear-gradient(135deg, var(--stone-light), var(--stone-dark) 60%, var(--stone-light));
    box-shadow: 0 6px 18px rgba(0,0,0,.25);
  }
  .flyer__inner {
    position: absolute; left: 38px; top: 32px;
    width: 524px; height: 792px;
    overflow: hidden;
    font-family: "PT Sans Narrow", "Arial Narrow", sans-serif;
  }
  .hero {
    position: absolute; left: 0; top: 0; width: 100%; height: 322px;
    background:
      radial-gradient(ellipse at 80% 20%, var(--leaf-dark), transparent 55%),
      linear-gradient(180deg, var(--leaf-light) 0%, var(--leaf-mid) 45%, var(--leaf-dark) 100%);
  }
  .hero__focus {
    position: absolute; left: 98px; top: 190px;
    width: 132px; height: 132px; border-radius: 50%;
    border: 4px solid var(--white);
    background: radial-gradient(circle, #3f5320, #1f2c0c);
  }
  .bubble {
    position: absolute; left: 114px; top: 24px;
    width: 350px; height: 102px;
    background: var(--white); border-radius: 8px;
    padding: 12px 16px;
    font-family: "Crimson Pro", Georgia, serif;
    font-weight: 500; font-size: 21px; line-height: 29px;
    color: #1a1a1a;
  }
  .bubble__tail {
    position: absolute; left: 44px; top: 100px;
  }
  .brand-band {
    position: absolute; left: 0; top: 322px; width: 100%; height: 77px;
    background: var(--cream);
    display: flex; align-items: center;
  }
  .brand {
    display: flex; align-items: center; gap: 8px;
    margin-left: 22px; width: 160px;
  }
  .brand__dot {
    width: 26px; height: 26px; border-radius: 50%;
    background: var(--headline-blue); flex: none;
  }
  .brand__name {
    font-size: 17px; font-weight: 700; color: var(--headline-blue);
    line-height: 1.05;
  }
  .tagline {
    flex: 1; text-align: right; padding-right: 14px;
    font-size: 24px; font-weight: 700; line-height: 27px;
    color: var(--headline-blue);
  }
  .pool {
    position: absolute; left: 0; top: 399px; width: 100%; height: 393px;
    background:
      repeating-linear-gradient(0deg, rgba(255,255,255,.08) 0 2px, transparent 2px 10px),
      repeating-linear-gradient(90deg, rgba(255,255,255,.08) 0 2px, transparent 2px 10px),
      linear-gradient(180deg, var(--pool-light), var(--pool-mid) 55%, var(--pool-deep));
  }
  .services {
    position: absolute; left: 0; top: 399px; width: 100%; height: 190px;
    display: grid; grid-template-columns: 226px 1fr;
    padding: 14px 0 0 18px;
    font-size: 17px; font-weight: 700; color: var(--navy);
  }
  .services__col { list-style: none; margin: 0; padding: 0; }
  .services__col li { height: 28px; line-height: 28px; white-space: nowrap; }
  .services__col li::before { content: "\2756\00a0"; font-size: 14px; }
  .price {
    position: absolute; left: 0; top: 589px; width: 100%; height: 84px;
    background: rgba(255,255,255,.55);
    text-align: center; font-weight: 700; line-height: 1;
  }
  .price__lead {
    display: block; margin-top: 10px;
    font-size: 30px; color: var(--price-blue);
    text-shadow: -1px -1px 0 var(--white), 1px -1px 0 var(--white), -1px 1px 0 var(--white), 1px 1px 0 var(--white), 0 0 3px var(--price-red);
  }
  .price__amount {
    display: block; margin-top: 4px;
    font-size: 33px; color: var(--white);
    text-shadow: -2px -2px 0 var(--price-red), 2px -2px 0 var(--price-red), -2px 2px 0 var(--price-red), 2px 2px 0 var(--price-red);
  }
  .contact {
    position: absolute; left: 140px; top: 680px;
    color: var(--navy);
  }
  .contact__label { font-size: 13px; margin-left: 6px; }
  .contact__phone { font-size: 35px; line-height: 40px; }
  .contact__email { font-size: 21px; line-height: 22px; }
</style>
</head>
<body>
  <article class="flyer">
    <div class="flyer__inner">
      <section class="hero" role="img" aria-label="Photo of a neglected green swimming pool beside a house and trees">
        <div class="hero__focus" role="img" aria-label="Close-up of algae in the pool water"></div>
      </section>
      <div class="bubble">
        Pool service frustrating you?<br>
        Troubled by poor water condition?<br>
        Tired of doing it yourself?
        <svg class="bubble__tail" width="22" height="20" viewBox="0 0 22 20"><path d="M0 0 H22 L6 20 Z" fill="#ffffff"/></svg>
      </div>

      <header class="brand-band">
        <div class="brand">
          <span class="brand__dot"></span>
          <span class="brand__name">Gumleaf Spa Care</span>
        </div>
        <h1 class="tagline">Keep your swimming pool<br>sparkling and safe all year round</h1>
      </header>

      <div class="pool" role="img" aria-label="Blue mosaic-tiled pool water"></div>

      <div class="services">
        <ul class="services__col">
          <li>Water testing</li>
          <li>Pool chemistry</li>
          <li>Chlorine levels</li>
          <li>Ph balance</li>
          <li>Equipment maintenance</li>
          <li>Algae prevention</li>
        </ul>
        <ul class="services__col">
          <li>Leaf and debris maintenance</li>
          <li>Filter cleaning</li>
          <li>Tile cleaning</li>
          <li>Salt water systems</li>
          <li>Local service</li>
          <li>Chemicals supplied and delivered</li>
        </ul>
      </div>

      <div class="price">
        <span class="price__lead">ALL FOR THE LOW PRICE OF</span>
        <span class="price__amount">$40 a Month + Plus chemicals</span>
      </div>

      <footer class="contact">
        <p class="contact__label">Contact details</p>
        <p class="contact__phone">Mitch - 0417 283 640</p>
        <p class="contact__email">gumleafspacare@quollmail.net.au</p>
      </footer>
    </div>
  </article>
</body>
</html>
```